Company Presentation / Image Presentation

Take the file attached and transform it into a modern and compelling design; fitting to the concepts and design language of our Homepage (lumbrivo.net) - but not just copy it - do an interpretation. We expect in the first step a Powerpoint - second step (not part on tis here) a Flyer. We will set up a second request.

Target Market(s)

Corporate companies across Europe

Industry/Entity Type

Corporate

Font styles to use
Sans Serif

Colors
3277b5
33a6d7
33b8a4

Requirements
Must have
• Modern style - in sync. with our HP http://www.lumbrivo.net
Nice to have
• https://www.linkedin.com/company/58204317
Should not have
• stupid stereotypes

```html
<!DOCTYPE html>
<html lang="en">
<head>
<meta charset="utf-8">
<title>SCALE IDEAS – Internal and External Factors</title>
<link href="https://fonts.googleapis.com/css2?family=Roboto:wght@400;500&family=Roboto+Condensed:wght@400;500;700&family=Montserrat:wght@600;700;800&display=swap" rel="stylesheet">
<style>
:root{
  --brand-blue:#3277b5;
  --brand-sky:#33a6d7;
  --brand-teal:#33b8a4;
  --navy:#173a5e;
  --ink:#22303c;
  --muted:#5b6b78;
  --panel-a:#eaf4fb;
  --panel-b:#e5f5f2;
  --seg-social:#33a6d7;
  --seg-autonomy:#3277b5;
  --seg-experiment:#1f5b92;
  --seg-dash:#2a8fc7;
  --seg-interface:#4aaed9;
  --seg-staff:#33b8a4;
  --seg-community:#1f8f7e;
  --seg-algorithm:#2e9fb0;
  --seg-leverage:#1b6f8a;
  --seg-engage:#3fb59a;
}
*{margin:0;padding:0;box-sizing:border-box}
html,body{width:1200px;height:671px;overflow:hidden;background:#fff}
.canvas{position:relative;width:1200px;height:671px;overflow:hidden;background:#fff;font-family:"Roboto Condensed",sans-serif;color:var(--ink)}
.top-band{position:absolute;left:0;top:0;width:1200px;height:20px;background:var(--navy)}
.bottom-band{position:absolute;left:0;bottom:0;width:1200px;height:22px;background:var(--navy)}
.right-edge{position:absolute;right:0;top:0;width:17px;height:671px;background:var(--navy)}
.side-band{position:absolute;left:0;top:0;width:42px;height:671px;background:linear-gradient(180deg,var(--brand-teal),var(--brand-sky))}
.external-panel{position:absolute;left:614px;top:20px;width:569px;height:629px;background:linear-gradient(160deg,var(--panel-a),var(--panel-b))}
.accent{position:absolute}
.accent-top{left:672px;top:0;width:12px;height:20px;background:var(--brand-teal)}
.accent-r1{left:1186px;top:402px;width:14px;height:11px;background:var(--brand-teal)}
.accent-r2{left:1186px;top:565px;width:14px;height:10px;background:var(--brand-sky)}
.accent-corner{left:1112px;top:0;width:71px;height:20px;background:var(--brand-blue);border-radius:0 0 0 40px}
.accent-foot{left:677px;top:649px;width:112px;height:22px;background:var(--brand-sky);border-radius:0 0 56px 56px}
.tab{position:absolute;top:0;height:29px;color:#fff;font-family:"Montserrat",sans-serif;font-weight:700;font-size:14px;line-height:29px;text-align:center;letter-spacing:.3px;border-radius:0 0 8px 8px}
.tab-internal{left:204px;width:253px;background:var(--brand-sky)}
.tab-external{left:768px;width:254px;background:var(--brand-teal)}
.band-title{position:absolute;left:21px;top:335px;transform:translate(-50%,-50%) rotate(-90deg);white-space:nowrap;color:#fff;font-family:"Roboto",sans-serif;font-weight:500;font-size:29px}
.band-motto{position:absolute;left:53px;top:535px;transform:translate(-50%,-50%) rotate(-90deg);white-space:nowrap;color:var(--navy);font-family:"Roboto",sans-serif;font-size:19px}
.headline{position:absolute;left:62px;top:34px;font-family:"Montserrat",sans-serif;font-weight:700;font-size:17px;color:var(--navy);white-space:nowrap}
.subline{position:absolute;left:62px;top:59px;font-family:"Roboto",sans-serif;font-size:14.3px;color:var(--brand-sky);white-space:nowrap}
.factor{position:absolute;font-size:12.3px;line-height:16.6px;white-space:nowrap;color:var(--ink)}
.factor::before{content:"";position:absolute;left:-20px;top:5px;width:6px;height:6px;border-radius:50%;background:var(--bullet)}
.factor .term{font-size:14px;font-weight:700;text-decoration:underline;text-decoration-thickness:1.5px;text-underline-offset:3px;color:var(--bullet)}
.f-social{left:99px;top:95px;--bullet:var(--seg-social)}
.f-autonomy{left:97px;top:152px;--bullet:var(--seg-autonomy)}
.f-experiment{left:98px;top:273px;--bullet:var(--seg-experiment)}
.f-dash{left:99px;top:445px;--bullet:var(--seg-dash)}
.f-interface{left:223px;top:525px;--bullet:var(--seg-interface)}
.f-staff{left:736px;top:52px;--bullet:var(--seg-staff)}
.f-community{left:825px;top:155px;--bullet:var(--seg-community)}
.f-algorithm{left:846px;top:290px;--bullet:var(--seg-algorithm)}
.f-leverage{left:841px;top:436px;--bullet:var(--seg-leverage)}
.f-engage{left:658px;top:544px;--bullet:var(--seg-engage)}
.brain-box{position:absolute;background:#fff;border-radius:8px;box-shadow:0 2px 8px rgba(23,58,94,.15);overflow:hidden;font-family:"Roboto",sans-serif}
.brain-box h3{color:#fff;font-family:"Montserrat",sans-serif;font-weight:600;font-size:11.5px;height:20px;line-height:20px;text-align:center}
.brain-left h3{background:var(--brand-blue)}
.brain-right h3{background:var(--brand-teal)}
.brain-box ul{list-style:none;padding:8px 0 0 9px;font-size:11.5px;line-height:16.8px;color:var(--ink)}
.brain-box li::before{content:"";display:inline-block;width:5px;height:5px;border-radius:50%;margin:0 8px 2px 0;background:var(--dot)}
.brain-left{left:77px;top:538px;width:111px;height:101px;--dot:var(--brand-blue)}
.brain-right{left:1045px;top:549px;width:124px;height:88px;--dot:var(--brand-teal)}
.brain-right ul{padding-top:7px}
.brain-mark{position:absolute;width:34px;height:34px;border-radius:50%}
.brain-left .brain-mark{left:70px;top:36px;background:var(--brand-blue)}
.brain-right .brain-mark{left:84px;top:36px;background:var(--brand-teal)}
.brain-mark::after{content:"";position:absolute;left:11px;top:11px;width:12px;height:12px;border:1.6px solid #fff;border-radius:50%}
.wheel{position:absolute;left:0;top:0}
.seg-label{font-family:"Roboto Condensed",sans-serif;font-weight:700;font-size:15px;fill:#fff;text-anchor:middle}
.hub-scale{font-family:"Montserrat",sans-serif;font-weight:800;font-size:34px;fill:var(--navy);text-anchor:middle;letter-spacing:.5px}
.hub-small{font-family:"Roboto Condensed",sans-serif;font-weight:500;font-size:9px;fill:var(--muted);text-anchor:middle}
.hub-growth{font-family:"Roboto Condensed",sans-serif;font-weight:700;font-size:13px;fill:var(--brand-blue);text-anchor:middle}
.icon-ring{fill:#fff;stroke-width:1.6}
.icon-line{fill:none;stroke-width:1.5;stroke-linecap:round;stroke-linejoin:round}
</style>
</head>
<body>
<div class="canvas">
  <div class="external-panel"></div>
  <div class="top-band"></div>
  <div class="bottom-band"></div>
  <div class="right-edge"></div>
  <div class="accent accent-top"></div>
  <div class="accent accent-corner"></div>
  <div class="accent accent-r1"></div>
  <div class="accent accent-r2"></div>
  <div class="accent accent-foot"></div>
  <div class="side-band"></div>
  <div class="band-title">Transitioning corporates towards Scaled Agility…</div>
  <div class="band-motto">Not more – not less.</div>

  <div class="tab tab-internal">Internal Factors</div>
  <div class="tab tab-external">External Factors</div>

  <h1 class="headline">Different people &amp; Different Processes SCALE IDEAS</h1>
  <p class="subline">Digitalization represents a Massive Transformation Purpose (MTP)</p>

  <svg class="wheel" width="1200" height="671" viewBox="0 0 1200 671" aria-label="SCALE IDEAS wheel">
    <g stroke="#fff" stroke-width="2">
      <path fill="var(--seg-staff)" d="M613 337 L613 142 A195 195 0 0 1 727.6 179.2 Z"/>
      <path fill="var(--seg-community)" d="M613 337 L727.6 179.2 A195 195 0 0 1 798.5 276.7 Z"/>
      <path fill="var(--seg-algorithm)" d="M613 337 L798.5 276.7 A195 195 0 0 1 798.5 397.3 Z"/>
      <path fill="var(--seg-leverage)" d="M613 337 L798.5 397.3 A195 195 0 0 1 727.6 494.8 Z"/>
      <path fill="var(--seg-engage)" d="M613 337 L727.6 494.8 A195 195 0 0 1 613 532 Z"/>
      <path fill="var(--seg-interface)" d="M613 337 L613 532 A195 195 0 0 1 498.4 494.8 Z"/>
      <path fill="var(--seg-dash)" d="M613 337 L498.4 494.8 A195 195 0 0 1 427.5 397.3 Z"/>
      <path fill="var(--seg-experiment)" d="M613 337 L427.5 397.3 A195 195 0 0 1 427.5 276.7 Z"/>
      <path fill="var(--seg-autonomy)" d="M613 337 L427.5 276.7 A195 195 0 0 1 498.4 179.2 Z"/>
      <path fill="var(--seg-social)" d="M613 337 L498.4 179.2 A195 195 0 0 1 613 142 Z"/>
    </g>
    <circle cx="613" cy="337" r="93" fill="#fff"/>
    <circle cx="613" cy="337" r="86" fill="none" stroke="var(--panel-a)" stroke-width="3"/>

    <text class="seg-label" x="560" y="178">Social</text>
    <text class="seg-label" x="557" y="197">Technologies</text>
    <text class="seg-label" x="657" y="188">Staff expert</text>
    <text class="seg-label" x="657" y="207">On demand</text>
    <text class="seg-label" x="730" y="251">Community</text>
    <text class="seg-label" x="730" y="270">&amp; crowd</text>
    <text class="seg-label" x="755" y="343">Algorithm</text>
    <text class="seg-label" x="731" y="418">Leveraged</text>
    <text class="seg-label" x="733" y="436">assets</text>
    <text class="seg-label" x="661" y="486">Engagement</text>
    <text class="seg-label" x="561" y="474">Interface</text>
    <text class="seg-label" x="558" y="492">processes</text>
    <text class="seg-label" x="491" y="426">Dashboards</text>
    <text class="seg-label" x="463" y="327">Ex-</text>
    <text class="seg-label" x="463" y="343">perimentation</text>
    <text class="seg-label" x="483" y="247">Autonomy</text>
    <text class="seg-label" x="484" y="266">Of teams</text>

    <text class="hub-scale" x="611" y="303">SCALE</text>
    <text class="hub-scale" x="611" y="334">IDEAS</text>
    <text class="hub-small" x="611" y="346">for the creation of</text>
    <text class="hub-growth" x="611" y="364">exponential growth within</text>
    <text class="hub-growth" x="611" y="380">your organization</text>

    <g stroke="var(--seg-social)">
      <circle class="icon-ring" cx="577" cy="125" r="17"/>
      <path class="icon-line" d="M569 131v-9h4l4-7c2 0 2 2 2 3l-1 4h5c1 0 2 1 2 2l-2 7h-10z M569 122h-3v9h3"/>
    </g>
    <g stroke="var(--seg-staff)">
      <circle class="icon-ring" cx="679" cy="131" r="17"/>
      <path class="icon-line" d="M672 124v1 M679 123v1 M686 124v1 M670 138v-9h4v9 M677 138v-10h4v10 M684 138v-9h4v9"/>
    </g>
    <g stroke="var(--seg-community)">
      <circle class="icon-ring" cx="789" cy="209" r="17"/>
      <path class="icon-line" d="M782 207a3 3 0 1 0 0.1 0 M777 217c1-4 9-4 10 0 M792 205a5 5 0 0 1 0 7 M795 202a9 9 0 0 1 0 13"/>
    </g>
    <g stroke="var(--seg-algorithm)">
      <circle class="icon-ring" cx="827" cy="381" r="17"/>
      <path class="icon-line" d="M820 371h14v20h-14z M822 374h10v4h-10z M823 382h1 M827 382h1 M831 382h1 M823 386h1 M827 386h1 M831 386h1"/>
    </g>
    <g stroke="var(--seg-leverage)">
      <circle class="icon-ring" cx="786" cy="483" r="17"/>
      <path class="icon-line" d="M778 492l9-9 M787 483a5 5 0 1 0 3-7l-3 3 2 2 3-3"/>
    </g>
    <g stroke="var(--seg-engage)">
      <circle class="icon-ring" cx="722" cy="522" r="17"/>
      <path class="icon-line" d="M713 522v0 M716 519v6 M719 515v14 M722 518v8 M725 514v16 M728 519v6 M731 522v0"/>
    </g>
    <g stroke="var(--seg-interface)">
      <circle class="icon-ring" cx="546" cy="544" r="17"/>
      <path class="icon-line" d="M538 542a8 8 0 0 1 14-4 M552 534v4h-4 M554 546a8 8 0 0 1-14 4 M540 554v-4h4"/>
    </g>
    <g stroke="var(--seg-dash)">
      <circle class="icon-ring" cx="432" cy="466" r="17"/>
      <path class="icon-line" d="M423 472a10 10 0 1 1 18 0 M432 470l5-7"/>
    </g>
    <g stroke="var(--seg-experiment)">
      <circle class="icon-ring" cx="396" cy="332" r="17"/>
      <path class="icon-line" d="M386 333h20a10 8 0 0 1-20 0z M392 342h8 M398 333l6-9"/>
    </g>
    <g stroke="var(--seg-autonomy)">
      <circle class="icon-ring" cx="438" cy="209" r="17"/>
      <path class="icon-line" d="M432 202h12l4 5-10 11-10-11z M428 207h20 M435 202l3 16 3-16"/>
    </g>
  </svg>

  <p class="factor f-social"><span class="term">Social Technologies</span> guarantee that communication channels will stay open. More<br>communication allows greater transparency, and importantly, keeps the organization always<br>connected to its massive transformative purpose (MTP).</p>

  <p class="factor f-autonomy"><span class="term">Autonomy</span> represents the key of the belief system of an ideal<br>ExO employee. ExOs need autonomous, multidisciplinary and<br>decentralized teams with the intention to satisfy the growing<br>demands of customers. The technology company “Brightloop”<br>for instance, implemented a quite extreme form of autonomy in<br>their organizational charter – the employees vote every quarter if<br>they want to keep their CEO.</p>

  <p class="factor f-experiment"><span class="term">Experimentation</span> is key to every ExO. Where<br>traditional Organizations sought to reduce every risk (for<br>various purposes) – they overlook the biggest risk. The<br>biggest risk is in fact taking no risk. If anyone wants to<br>succeeds – to experiment is a must. Caramia<br>Foods, a multinational confectionary company,<br>employs “Garages” to support the employees to anticipate<br>innovative ideas. Disconnected from outside contact,<br>participants can focus on the problem at hand rising with<br>the new solutions.</p>

  <p class="factor f-dash"><span class="term">Dashboards</span> enable people in their organization to<br>access relevant data in real time. Think of a dashboard within<br>a multiplayer game like “Realm of Ember”. You always know<br>where to go, how to get there and what to do once you will be<br>there.</p>

  <p class="factor f-interface"><span class="term">Interfaces</span> connect the SCALE externalities –<br>such as your community - with the company’s internal<br>workings. ExOs demand on interfaces to manage work and<br>projects and push them into the world. Currently Orchardia’s<br>App-Store is representing a fully developed interface, as it<br>allows customers to see what is available, and what’s more,<br>it’s indispensable to Orchardia and all its products.</p>

  <p class="factor f-staff">Having the right <span class="term">Staff (experts)</span> engaged on demand is definitely crucial for an ExO.<br>In most of the cases exceptionally performing organizations maintain a relatively small<br>group of specialized people. The workforce is expanded and enriched by excellent,<br>creative and flexible contractors whenever needed. Veltora (Austria's greatest insurance<br>company) uses contractors for nearly 50 percent of their IT-department.</p>

  <p class="factor f-community">Maintaining a <span class="term">Community and a crowd</span>, both lower the risk as<br>well as the effort to be invested to operate the business. Your<br>community is your core team, your user, your customers, your<br>company’s alumni as well as your company’s vendors, your partners<br>and your fans. The crowd is everyone outside your on-demand staff,<br>or people you engage for validation purposes – crowdsourcing or<br>even crowdfunding.</p>

  <p class="factor f-algorithm"><span class="term">Algorithms</span> sound far more complex than they really are.<br>This term stands just for a more or less complex sequence of<br>defined process steps within a predicable workflow. In business<br>we call them “End-2-End processes” – in Gridwise “Macros” and in<br>Mathematics “f(x)”. Search algorithms (a defined set of<br>automated operations) made Searchwell the world’s leading search<br>engine, some HR-departments use algorithms to prevent<br>biases in filling open positions.</p>

  <p class="factor f-leverage"><span class="term">Leverage assets</span> It is not necessary to own assets anymore<br>– you just need access to them. Stay flexible about them, too!<br>Only a few companies still need to own assets (like Parcelon owns<br>the warehouses they operate in). The minute your company’s<br>operations are based on real-time and consistent (zero latency)<br>information the situation is significantly different.</p>

  <p class="factor f-engage"><span class="term">Engagement</span> as well as the delivery of “purpose &amp; sense” is crucial for<br>the information based ExO-company approach. Networks, gamification and<br>constructive competition and positive feedback loops are options of<br>engaging people and deploying purpose &amp; sense to them. Engagement<br>and contextualization help inject your company with new ideas, paving the<br>way for innovation.</p>

  <div class="brain-box brain-left">
    <h3>Left brain</h3>
    <ul><li>Order</li><li>Control</li><li>Stability</li></ul>
    <span class="brain-mark"></span>
  </div>
  <div class="brain-box brain-right">
    <h3>Right brain</h3>
    <ul><li>Creativity</li><li>Growth</li><li>Uncertainty</li></ul>
    <span class="brain-mark"></span>
  </div>
</div>
</body>
</html>
```